Asian Pakistani: Wedding Invitation

Design a pakistani asian wedding invitation.
Islamic theme, with arabic text:

Text to be used:

Start with: bismillah and dua for marriage. (The Holy Quran chapter 25 verse 75 with arabic text and english translation below)

Mrs. Rubina Sohail wife of (late) Mr. Sohail Imran Qureshi
Cordially requests your company to grace the joyous occasion of the wedding of their beloved daughter
Mehreen Qureshi
Daughter of ( late) Mr Sohail Imran qureshi
with
Bilal Siddiqui
Son of Mr. Junaid Siddiqui & Mrs Shazia Siddiqui

Insha’Allah on Thursday 29th August 2019 at Velvet Orchard
12 Marlow Crescent, Croydon
CR7 2LP
Baraat Arrival 6:30

RSVP
Usman Qureshi 07700 900412
Tariq Mehmood 07700 900583
Faisal Butt 07700 900735

Target Market(s)

Muslims

Font styles to use
Script

Colors

Designer to choose colors to be used in the design.

Requirements
Must have
• stylish calligraphy Arabic lettering of the dua requested above
• Size:
• Long 4" x 9.5"
Nice to have
• ottoman empire: Art theme

```html
<!DOCTYPE html>
<html lang="en">
<head>
<meta charset="utf-8">
<title>Wedding Invitation – Mehreen &amp; Bilal</title>
<link href="https://fonts.googleapis.com/css2?family=Aladin&family=Amiri:ital,wght@0,400;0,700;1,400&family=Aref+Ruqaa:wght@700&family=Noto+Nastaliq+Urdu&display=swap" rel="stylesheet">
<style>
  :root {
    --paper: #ffffff;
    --ink: #111111;
    --grey-ink: #6e6e6e;
    --grey-soft: #8a8a8a;
    --violet-deep: #2c0b5e;
    --violet: #4b1796;
    --blush: #f6cdd3;
  }
  * { margin: 0; padding: 0; box-sizing: border-box; }
  html, body { width: 1200px; height: 2850px; overflow: hidden; background: var(--paper); }
  .invitation { position: relative; width: 1200px; height: 2850px; background: var(--paper); overflow: hidden; }

  .mandala { position: absolute; }
  .mandala--top { left: 0; top: 0; width: 540px; height: 540px; }
  .mandala--bottom { right: 0; bottom: 0; width: 560px; height: 720px; }

  .heading {
    position: absolute; top: 560px; left: 0; width: 1200px; text-align: center;
    font-family: "Aladin", cursive; font-weight: 400; font-size: 72px; color: var(--ink); letter-spacing: 1px;
  }
  .bismillah {
    position: absolute; top: 660px; left: 300px; width: 600px; text-align: center;
    font-family: "Aref Ruqaa", serif; font-weight: 700; font-size: 46px; color: var(--grey-ink);
  }
  .bismillah-translation {
    position: absolute; top: 770px; left: 0; width: 1200px; text-align: center;
    font-family: "Amiri", serif; font-style: italic; font-size: 24px; color: var(--grey-ink);
  }
  .verse {
    position: absolute; top: 862px; left: 60px; width: 1080px; text-align: center;
    font-family: "Amiri", serif; font-size: 40px; line-height: 70px; color: var(--grey-ink);
    direction: rtl; white-space: nowrap;
  }
  .verse-number { font-size: 30px; }
  .verse-translation {
    position: absolute; top: 960px; left: 120px; width: 960px; text-align: center;
    font-family: "Amiri", serif; font-style: italic; font-size: 25px; line-height: 38px; color: var(--grey-ink);
  }
  .verse-reference {
    position: absolute; top: 1024px; right: 100px;
    font-family: "Amiri", serif; font-style: italic; font-size: 19px; color: var(--grey-soft);
  }

  .poem {
    position: absolute; top: 1110px; left: 110px; width: 980px;
    display: flex; flex-direction: row; justify-content: space-between;
    font-family: "Noto Nastaliq Urdu", serif; font-size: 20px; color: var(--grey-ink); direction: rtl;
  }
  .poem-column { width: 460px; }
  .poem-column p { height: 52px; line-height: 52px; text-align: right; white-space: nowrap; }

  .details {
    position: absolute; top: 1342px; left: 70px; width: 1130px; text-align: center;
    font-family: "Aladin", cursive; font-size: 37px; line-height: 57.5px; color: var(--ink);
  }
  .details p { white-space: nowrap; }
</style>
</head>
<body>
<main class="invitation">
  <svg class="mandala mandala--top" viewBox="0 0 540 540" role="img" aria-label="Purple, black and blush ornamental mandala in the top left corner">
    <defs>
      <radialGradient id="mandalaTopTone" cx="140" cy="140" r="390" gradientUnits="userSpaceOnUse">
        <stop offset="0" stop-color="#4b1796"/>
        <stop offset="0.75" stop-color="#2c0b5e"/>
        <stop offset="1" stop-color="#f6cdd3"/>
      </radialGradient>
    </defs>
    <circle cx="140" cy="140" r="390" fill="url(#mandalaTopTone)"/>
  </svg>

  <h1 class="heading">bismillah and dua for marriage</h1>
  <p class="bismillah" lang="ar">بِسْمِ اللَّهِ الرَّحْمَٰنِ الرَّحِيمِ</p>
  <p class="bismillah-translation">In the name of Allah, the most Gracious, most Merciful</p>

  <p class="verse" lang="ar">رَبَّنَا هَبْ لَنَا مِنْ أَزْوَاجِنَا وَذُرِّيَّاتِنَا قُرَّةَ أَعْيُنٍ وَاجْعَلْنَا لِلْمُتَّقِينَ إِمَامًا <span class="verse-number">﴿٧٥﴾</span></p>
  <p class="verse-translation">Our Lord, grant us of our wives and children the delight of our eyes, and make us<br>a model of&nbsp; the righteous</p>
  <p class="verse-reference">(Sura Al-Furqan:75)</p>

  <section class="poem" lang="ur">
    <div class="poem-column">
      <p>اے میرے دل کے پیارے اے مہرباں ہمارے</p>
      <p>یہ فضل کر کہ ہوویں نیکو گہر یہ سارے</p>
      <p>سن میرے پیارے باری میری دعائیں ساری</p>
      <p>اپنی پناہ میں رکھیو سن کر یہ میری زاری</p>
    </div>
    <div class="poem-column">
      <p>کر ان کے نام روشن جیسے کہ ہیں ستارے</p>
      <p>یہ روز کر مبارک سُبْحَانَ مَنْ یَّرَانِیْ</p>
      <p>رحمت سے ان کو رکھنا میں تیرے منہ کے واری</p>
      <p>یہ روز کر مبارک سُبْحَانَ مَنْ یَّرَانِیْ</p>
    </div>
  </section>

  <section class="details">
    <p>Mrs. Rubina Sohail wife of (late) Mr. Sohail Imran Qureshi</p>
    <p>Cordially requests your company to grace the joyous occasion of the</p>
    <p>wedding of their beloved daughter Mehreen Qureshi</p>
    <p>Daughter of ( late) Mr Sohail Imran qureshi</p>
    <p>with Bilal Siddiqui Son of Mr. Junaid Siddiqui</p>
    <p>&amp; Mrs Shazia Siddiqui</p>
    <p>Insha’Allah on Thursday 29th August 2019 at Velvet Orchard</p>
    <p>12 Marlow Crescent, Croydon</p>
    <p>CR7 2LP</p>
    <p>Baraat Arrival 6:30</p>
    <p>RSVP</p>
    <p>Usman Qureshi 07700 900412</p>
    <p>Tariq Mehmood 07700 900583</p>
    <p>Faisal Butt 07700 900735</p>
  </section>

  <svg class="mandala mandala--bottom" viewBox="0 0 560 720" role="img" aria-label="Purple, black and blush ornamental mandala in the bottom right corner">
    <defs>
      <radialGradient id="mandalaBottomTone" cx="422" cy="589" r="405" gradientUnits="userSpaceOnUse">
        <stop offset="0" stop-color="#4b1796"/>
        <stop offset="0.75" stop-color="#2c0b5e"/>
        <stop offset="1" stop-color="#f6cdd3"/>
      </radialGradient>
    </defs>
    <circle cx="422" cy="589" r="405" fill="url(#mandalaBottomTone)"/>
  </svg>
</main>
</body>
</html>
```